My Plain 4 Posh Affairs Flyer...Transforming Ordinary into Extraordinary!

I need a flyer that will show what my business represents. Our ultimate goal is to transform any setting from blah (boring and dull) to bliss (serene joy and happiness). I attached my logo and pictures of some of our work that I would like to be on the flyer.

Plain 4 Posh Affairs is a event planning and decor design experts.

Hello fellow designers! Please take a look at my flyer project! I look forward to your amazing designs!

Target Market(s)

Clients with unlimited budgets to clients with reasonable budgets

Industry/Entity Type

Event Planning

Font styles to use
Serif
Script

Requirements
Must have
• My logo
• Pictures of events
• Eye catching fonts and graphics
• I need a simple captive phrase that will capture the readers attention.
• Contact information: plain4posh@mailvane.net
• Call today! Ask for Rochelle @ (555) 318-4602 or (555) 427-9153
• I want to include words that start with the letter b.
• example: Don't be boring!!! Be Blissed!!!!
• I not sure. I'm stuck on this!
Nice to have
• I would like to see before and after pics. Like as room or venue that is blah (dull, ugly, and unappealing). A picture beside it that is full of bliss (the wedding photo beside it). I basically want to show transformation
Should not have
• Boring fonts or graphics

```html
<!DOCTYPE html>
<html lang="en">
<head>
<meta charset="utf-8">
<title>Plain 4 Posh Affairs Flyer</title>
<link rel="stylesheet" href="https://fonts.googleapis.com/css2?family=Lobster&family=Lato:wght@400;700&display=swap">
<style>
  :root {
    --magenta: #b0255c;
    --magenta-deep: #8e1846;
    --ink: #2e2a2c;
    --body-text: #2a2a2a;
    --paper: #ffffff;
    --swoosh: #0d0d0d;
    --page-bg: #f2f2f2;
  }
  html, body {
    margin: 0;
    padding: 0;
    width: 920px;
    height: 1200px;
    overflow: hidden;
    background: var(--page-bg);
  }
  .flyer {
    position: relative;
    width: 920px;
    height: 1200px;
    overflow: hidden;
    font-family: "Lato", Arial, sans-serif;
    color: var(--body-text);
  }
  .flyer-art {
    position: absolute;
    inset: 0;
  }
  .brand-badge {
    position: absolute;
    left: 72px;
    top: 322px;
    width: 266px;
    height: 266px;
    display: flex;
    align-items: center;
    justify-content: center;
  }
  .brand-name {
    font-family: "Lato", Arial, sans-serif;
    font-weight: 700;
    font-size: 30px;
    color: var(--magenta-deep);
    letter-spacing: 0.5px;
  }
  .headline {
    position: absolute;
    left: 40px;
    top: 585px;
    margin: 0;
    font-family: "Lobster", cursive;
    font-weight: 400;
    font-style: italic;
    font-size: 46px;
    color: var(--magenta);
    line-height: 1;
    white-space: nowrap;
  }
  .subline {
    position: absolute;
    left: 40px;
    top: 645px;
    margin: 0;
    font-family: "Lobster", cursive;
    font-style: italic;
    font-size: 34px;
    color: var(--ink);
    line-height: 1;
    white-space: nowrap;
  }
  .section-tab {
    position: absolute;
    left: 0;
    top: 738px;
    width: 200px;
    height: 46px;
    background: var(--magenta);
    border-radius: 0 23px 23px 0;
    color: var(--paper);
    font-family: "Lobster", cursive;
    font-style: italic;
    font-size: 27px;
    line-height: 46px;
    padding-left: 48px;
    box-sizing: border-box;
  }
  .about-copy {
    position: absolute;
    left: 31px;
    top: 800px;
    width: 770px;
    margin: 0;
    font-size: 17.5px;
    line-height: 24px;
  }
  .about-copy .contact {
    color: var(--magenta-deep);
  }
  .serve-title {
    position: absolute;
    right: 152px;
    top: 902px;
    margin: 0;
    font-family: "Lobster", cursive;
    font-style: italic;
    font-weight: 400;
    font-size: 30px;
    color: var(--magenta);
  }
  .serve-list {
    position: absolute;
    right: 152px;
    top: 950px;
    margin: 0;
    padding: 0;
    list-style: none;
    text-align: right;
    font-size: 17.5px;
    line-height: 24px;
  }
  .serve-list li {
    position: relative;
    margin-bottom: 7px;
  }
  .serve-list li::after {
    content: "";
    position: absolute;
    right: -20px;
    top: 9px;
    width: 7px;
    height: 7px;
    border-radius: 50%;
    background: var(--magenta);
  }
</style>
</head>
<body>
<main class="flyer">
  <svg class="flyer-art" width="920" height="1200" viewBox="0 0 920 1200" xmlns="http://www.w3.org/2000/svg">
    <defs>
      <linearGradient id="rosesTone" x1="0" y1="0" x2="1" y2="1">
        <stop offset="0" stop-color="#c9d49a"/>
        <stop offset="0.25" stop-color="#d23a52"/>
        <stop offset="0.6" stop-color="#b81f3a"/>
        <stop offset="0.85" stop-color="#e9a6a4"/>
        <stop offset="1" stop-color="#dfe5b8"/>
      </linearGradient>
      <linearGradient id="panelTone" x1="0" y1="0" x2="0" y2="1">
        <stop offset="0" stop-color="#c2306a"/>
        <stop offset="0.5" stop-color="#b7255f"/>
        <stop offset="1" stop-color="#a81e55"/>
      </linearGradient>
      <radialGradient id="floralHaze" cx="0.5" cy="0.4" r="0.6">
        <stop offset="0" stop-color="#d8557f" stop-opacity="0.8"/>
        <stop offset="1" stop-color="#b7255f" stop-opacity="0"/>
      </radialGradient>
      <radialGradient id="paperTone" cx="0.55" cy="0.45" r="0.75">
        <stop offset="0" stop-color="#ffffff"/>
        <stop offset="0.7" stop-color="#f1f1f1"/>
        <stop offset="1" stop-color="#d9d9d9"/>
      </radialGradient>
      <linearGradient id="banquetTone" x1="0" y1="0" x2="0" y2="1">
        <stop offset="0" stop-color="#f4efe6"/>
        <stop offset="0.45" stop-color="#e9e4ee"/>
        <stop offset="0.7" stop-color="#8b3fa8"/>
        <stop offset="1" stop-color="#f2f2f4"/>
      </linearGradient>
      <linearGradient id="stageTone" x1="0" y1="0" x2="0" y2="1">
        <stop offset="0" stop-color="#2a4b9a"/>
        <stop offset="0.45" stop-color="#1a1a1f"/>
        <stop offset="0.75" stop-color="#d9c9a8"/>
        <stop offset="1" stop-color="#b98a55"/>
      </linearGradient>
    </defs>

    <rect class="panel-magenta" width="920" height="1200" fill="url(#panelTone)"/>
    <rect class="panel-floral" role="img" aria-label="Soft faded photo of a pink floral arrangement" x="480" y="220" width="440" height="500" fill="url(#floralHaze)"/>

    <path class="hero-photo" role="img" aria-label="Photo of a red rose and pink blossom bouquet"
          d="M0,0 H920 V165 C770,330 560,432 330,440 L0,448 Z" fill="url(#rosesTone)"/>
    <path class="hero-swoosh" d="M330,440 C560,432 770,330 920,165 V225 C770,380 560,455 330,458 Z" fill="var(--swoosh)"/>

    <path class="content-swoosh" d="M0,450 V1200 H840 C890,960 950,720 840,590 C730,470 530,445 330,448 Z" fill="var(--swoosh)"/>
    <path class="content-paper" d="M0,470 V1200 H805 C850,960 905,735 805,612 C705,500 520,470 330,470 Z" fill="url(#paperTone)"/>

    <circle class="badge-frame" cx="205" cy="455" r="133" fill="var(--paper)" stroke="var(--swoosh)" stroke-width="3"/>

    <circle class="event-photo" role="img" aria-label="Photo of a banquet hall with white chair covers and purple sashes"
            cx="110" cy="1040" r="155" fill="url(#banquetTone)" stroke="var(--magenta)" stroke-width="5"/>
    <circle class="event-photo" role="img" aria-label="Photo of an event stage with a blue curtain"
            cx="318" cy="1066" r="115" fill="url(#stageTone)" stroke="var(--magenta)" stroke-width="5"/>
  </svg>

  <div class="brand-badge"><span class="brand-name">Plain 4 Posh</span></div>

  <h1 class="headline">Don't be boring... Be Blissed!</h1>
  <p class="subline">Transforming ordinary into extraordinary</p>

  <div class="section-tab">About Us</div>
  <p class="about-copy">Plain 4 Posh Affairs are event planning and decor design experts, turning any setting from boring and dull into beautiful bliss. <span class="contact">Call today! Ask for Rochelle @ (555) 318-4602 or (555) 427-9153, or write to plain4posh@mailvane.net</span></p>

  <h2 class="serve-title">We Serve</h2>
  <ul class="serve-list">
    <li>Weddings and beautiful receptions<br>Bridal and baby showers, birthdays and<br>milestone celebrations.</li>
    <li>Banquets and business galas.</li>
    <li>Venue and ballroom decor.</li>
    <li>Budgets big and small alike.</li>
    <li>Full planning, start to finish.</li>
  </ul>
</main>
</body>
</html>
```